Change of Address Card

We are fertility physicians in New York . Need a change of address postcard .

The front should be colorful
contain the statement " we are moving!"
and the names Marcus Tolleson MD, Helen Brisco MD

Also the front should contain the drawing of a sperm with either wings or wheeels or whatever your creativity suggests as long as it is not vulgar ( we are doctors !)

The back should contain
the address area and stamp area
and a text area
and possibly a recall of the drawing in front.
use same font

text below

Dear Friends and Colleagues

Marcus and Helen are relocating their fertility practice to a new location on 418 West 91st Street, Suite 2207, New York NY 10024
Please take note of our new phone number
Our New phone Number is 212-640-5193

Thank you for your support!

Target Market(s)

this is a card that goes to physicians

Industry/Entity Type

It Support

Requirements
Must have
• fit standard postcard size
Rectangular
At least 3-1/2 inches high x 5 inches long x 0.007 inch thick
No more than 4-1/4 inches high x 6 inches long x 0.016 inches thick
will not be mailed in an envelope

```html
<!DOCTYPE html>
<html lang="en">
<head>
<meta charset="utf-8">
<title>We Are Moving – Change of Address Postcard</title>
<link rel="stylesheet" href="https://fonts.googleapis.com/css2?family=Poppins:wght@300;400;500;600;700&display=swap">
<style>
  :root {
    --page: #ffffff;
    --card: #ffffff;
    --card-edge: #b9b9b9;
    --brand-blue: #6497f5;
    --soft-blue: #a9c3f7;
    --soft-blue-faint: #e7eefc;
    --ink: #111111;
    --accent-red: #f5161a;
    --body-gray: #555a5e;
    --rule-gray: #9aa0a3;
    --stamp-edge: #a9adaf;
    --stamp-text: #e3e7e8;
  }
  * { box-sizing: border-box; margin: 0; padding: 0; }
  html, body {
    width: 1185px;
    height: 1200px;
    overflow: hidden;
    background: var(--page);
  }
  .layout {
    position: relative;
    width: 1200px;
    height: 1215px;
    transform: scale(0.9875);
    transform-origin: 0 0;
    font-family: "Poppins", sans-serif;
  }
  .postcard {
    position: absolute;
    left: 200px;
    width: 726px;
    height: 494px;
    background: var(--card);
    border: 1px solid var(--card-edge);
    overflow: hidden;
  }
  .postcard--front { top: 51px; }
  .postcard--back { top: 647px; }

  .postcard__shapes {
    position: absolute;
    inset: 0;
    width: 100%;
    height: 100%;
  }

  .motif {
    position: absolute;
    border-radius: 48%;
  }
  .motif--front-top {
    left: 18px; top: 0; width: 440px; height: 210px;
    background: radial-gradient(ellipse at 50% 55%, var(--soft-blue-faint) 0%, rgba(231,238,252,0) 72%);
  }
  .motif--front-bottom {
    left: 290px; top: 220px; width: 250px; height: 260px;
    background: radial-gradient(ellipse at 45% 55%, var(--soft-blue-faint) 0%, rgba(231,238,252,0) 72%);
  }
  .motif--back {
    left: 140px; top: 25px; width: 210px; height: 125px;
    background: radial-gradient(ellipse at 40% 55%, var(--soft-blue-faint) 0%, rgba(231,238,252,0) 72%);
  }

  .headline {
    position: absolute;
    left: 30px;
    top: 212px;
    font-weight: 600;
    font-size: 72px;
    line-height: 83px;
    letter-spacing: -1px;
  }
  .headline__line { display: block; }
  .headline__we { color: var(--ink); }
  .headline__are { color: #ffffff; }
  .headline__moving { color: var(--accent-red); }
  .headline__moving-o { color: var(--ink); }

  .physicians {
    position: absolute;
    left: 372px;
    top: 175px;
    font-weight: 600;
    font-size: 29px;
    line-height: 36px;
    color: var(--ink);
    white-space: pre;
  }

  .message {
    position: absolute;
    left: 29px;
    top: 176px;
    color: var(--body-gray);
    font-size: 17px;
    line-height: 21.5px;
  }
  .message__greeting { font-weight: 600; margin-bottom: 21px; }
  .message__body { font-weight: 300; font-size: 17.5px; margin-bottom: 21px; }
  .message__contact { font-weight: 600; margin-bottom: 21px; }
  .message__thanks { font-weight: 600; }

  .stamp-area {
    position: absolute;
    left: 562px;
    top: 45px;
    width: 118px;
    height: 117px;
    border: 2px solid var(--stamp-edge);
    color: var(--stamp-text);
    font-weight: 600;
    font-size: 26px;
    line-height: 37px;
    text-align: center;
    padding-top: 20px;
  }

  .address-lines {
    position: absolute;
    left: 456px;
    top: 281px;
    width: 224px;
    list-style: none;
  }
  .address-lines li {
    height: 31px;
    border-bottom: 1.5px solid var(--rule-gray);
  }
  .address-lines li:first-child { height: 1px; }
</style>
</head>
<body>
<main class="layout">

  <section class="postcard postcard--front" aria-label="Postcard front">
    <div class="motif motif--front-top" role="img" aria-label="Playful swimming sperm drawings trailing 'we are moving' lettering"></div>
    <div class="motif motif--front-bottom" role="img" aria-label="Group of swimming sperm drawings trailing 'we are moving' lettering"></div>
    <svg class="postcard__shapes" viewBox="0 0 726 494" aria-hidden="true">
      <circle cx="79" cy="389" r="227" fill="var(--brand-blue)"/>
    </svg>
    <h1 class="headline">
      <span class="headline__line headline__we">We</span>
      <span class="headline__line headline__are">are</span>
      <span class="headline__line headline__moving">m<span class="headline__moving-o">o</span>ving</span>
    </h1>
    <p class="physicians">Marcus Tolleson   MD
Helen Brisco   MD</p>
  </section>

  <section class="postcard postcard--back" aria-label="Postcard back">
    <svg class="postcard__shapes" viewBox="0 0 726 494" aria-hidden="true">
      <circle cx="-21" cy="18" r="150" fill="var(--brand-blue)"/>
    </svg>
    <div class="motif motif--back" role="img" aria-label="Small sperm drawing with 'we are moving' lettering, echoing the front"></div>

    <div class="stamp-area">STAMP<br>AREA</div>

    <ul class="address-lines" aria-label="Recipient address lines">
      <li></li><li></li><li></li><li></li>
    </ul>

    <div class="message">
      <p class="message__greeting">Dear Friends And Colleagues,</p>
      <p class="message__body">Dr. Helen Brisco and Dr. Marcus Tolleson<br>have moved their fertility practice to<br>a new location. Our new address is:</p>
      <p class="message__contact">418 West 91st Street, Suite 2207<br>New York, NY 10024<br>Tel : (212)6405193<br>Email : Tolleson@northpointmail.net</p>
      <p class="message__thanks">Thank You for Your Support!</p>
    </div>
  </section>

</main>
</body>
</html>
```